Adult Literacy Program - flyer to attract volunteers and students

We want a flyer that is engaging, colorful, modern and will appeal to our primary audience of adults aged 40-60. We are trying to attract both prospective volunteers (typically age 50+, mostly women) and students (typically aged 40+).
The flyer should feature diverse people working together in pairs of two, reading or talking, with a workbook or some reading material in front of them.

Our organization trains tutors to work one-on-one with adults who are learning how to read. Most of our adult students are non-native speakers of English. Many are of Haitian or Hispanic origin, so we would like some people who represent that demographic.

The Flyer should represent reading, learning, literacy, knowledge, growth,
and opportunities.
Our students are learning to read so they can advance their job opportunities.

Target Market(s)

Adults aged 40-60, primarily women, retired, volunteers

Industry/Entity Type

Education

Font styles to use
Serif
Sans Serif

Colors

Designer to choose colors to be used in the design.

Requirements
Must have
• - UPDATE: Should be designed as a TRI-FOLD brochure on 8.5 x 11 inch paper that will be folded into thirds.
• - Images of diverse people, women and men, who look Hispanic, Haitian and other nationalities as well as Caucasian.
• - Our logo on the front cover
Nice to have
• The sample flyer is very boring and dry! We are open to different ways of presenting the text.

```html
<!DOCTYPE html>
<html lang="en">
<head>
<meta charset="utf-8">
<title>Reading Bridge Partners – Tri-fold Brochure</title>
<link rel="stylesheet" href="https://fonts.googleapis.com/css2?family=Poppins:wght@600;700;800&display=swap">
<style>
  :root {
    --navy: #0b1f5e;
    --white: #ffffff;
    --sky: #1aa3d9;
    --page: #ffffff;
    --fold: #ffffff;
    --shadow: rgba(0,0,0,0.18);
  }
  * { margin: 0; padding: 0; box-sizing: border-box; }
  html, body { width: 1200px; height: 1200px; overflow: hidden; background: var(--page); }
  body { position: relative; font-family: "Poppins", Arial, sans-serif; color: var(--white); text-transform: uppercase; }

  .sheet { position: absolute; left: 218px; width: 707px; height: 546px; background: var(--navy); box-shadow: 6px 6px 10px var(--shadow); overflow: hidden; }
  .sheet--inside { top: 30px; }
  .sheet--outside { top: 598px; }
  .sheet-art { position: absolute; inset: 0; width: 707px; height: 546px; }

  .pill { position: absolute; background: var(--white); color: var(--navy); font-weight: 800; line-height: 1; display: flex; align-items: center; }
  .pill--students { left: 0; top: 367px; width: 222px; height: 38px; border-radius: 0 19px 19px 0; padding-left: 8px; font-size: 34px; }
  .pill--volunteer { left: 484px; top: 376px; width: 223px; height: 38px; border-radius: 19px 0 0 19px; padding-left: 12px; font-size: 33px; }
  .pill--tutors { left: 496px; top: 312px; width: 211px; height: 43px; border-radius: 22px 0 0 22px; padding-left: 30px; font-size: 40px; }

  .student-list { position: absolute; left: 12px; top: 410px; width: 222px; font-size: 11px; font-weight: 700; line-height: 12.8px; list-style: none; white-space: nowrap; }
  .student-list li { padding-left: 3px; }
  .student-list .bullet::before { content: "· "; }

  .brand-tab { position: absolute; left: 302px; top: 0; width: 102px; height: 110px; background: var(--white); border-radius: 0 0 51px 51px; display: flex; align-items: flex-end; justify-content: center; padding-bottom: 24px; }
  .brand-badge { position: absolute; left: 612px; top: 0; width: 92px; height: 114px; background: var(--white); border-radius: 0 0 46px 46px; display: flex; align-items: flex-end; justify-content: center; padding-bottom: 26px; }
  .brand-name { color: var(--sky); font-weight: 700; font-size: 9px; line-height: 11px; text-align: center; }
  .brand-mark { display: block; width: 14px; height: 14px; border-radius: 50%; background: var(--sky); margin: 0 auto 6px; }

  .cta-box { position: absolute; left: 235px; top: 121px; width: 236px; height: 53px; background: var(--white); color: var(--navy); font-weight: 800; font-size: 16.4px; line-height: 17.6px; text-align: center; padding-top: 0; }
  .contact { position: absolute; left: 235px; top: 180px; width: 236px; text-align: center; font-weight: 700; font-size: 13px; line-height: 15.2px; white-space: nowrap; }
  .contact .email { font-size: 12.6px; margin-top: 3px; }

  .volunteer-copy { position: absolute; left: 484px; top: 433px; width: 220px; font-weight: 800; font-size: 18.4px; line-height: 20.8px; white-space: nowrap; }
  .volunteer-copy .spread { letter-spacing: 1.3px; }

  .tutor-points { position: absolute; left: 12px; top: 385px; width: 672px; text-align: right; font-weight: 800; font-size: 18.6px; line-height: 20.8px; list-style: none; white-space: nowrap; }
  .tutor-points li::after { content: " •"; }
  .tutor-points li.closing { padding-right: 14px; }
  .tutor-points li.closing::after { content: ""; }
</style>
</head>
<body>

<section class="sheet sheet--inside">
  <svg class="sheet-art" viewBox="0 0 707 546">
    <defs>
      <linearGradient id="studentsPhoto" x1="0" y1="0" x2="1" y2="1">
        <stop offset="0" stop-color="#3a3a40"/><stop offset="0.5" stop-color="#b9a48e"/><stop offset="1" stop-color="#3a8fb8"/>
      </linearGradient>
      <linearGradient id="pairPhoto" x1="0" y1="0" x2="1" y2="1">
        <stop offset="0" stop-color="#9aa06a"/><stop offset="0.5" stop-color="#c9a58a"/><stop offset="1" stop-color="#e9e2d2"/>
      </linearGradient>
      <linearGradient id="volunteerPhoto" x1="0" y1="0" x2="1" y2="1">
        <stop offset="0" stop-color="#8a6a4a"/><stop offset="0.5" stop-color="#e6d2c2"/><stop offset="1" stop-color="#c9a07a"/>
      </linearGradient>
    </defs>
    <path role="img" aria-label="Photo: a tutor and an adult student reading together at a library table" d="M0 0 H235 V250 Q140 330 0 352 Z" fill="url(#studentsPhoto)"/>
    <path d="M0 356 Q150 336 235 254" fill="none" stroke="var(--white)" stroke-width="7"/>
    <path role="img" aria-label="Photo: a smiling woman holding a workbook talking with a man" d="M235 346 Q360 268 471 254 V546 H235 Z" fill="url(#pairPhoto)"/>
    <path d="M235 344 Q360 266 471 252" fill="none" stroke="var(--white)" stroke-width="5"/>
    <path role="img" aria-label="Photo: a smiling young man holding a book in front of library shelves" d="M471 0 H707 V250 Q620 330 471 342 Z" fill="url(#volunteerPhoto)"/>
    <path d="M471 346 Q620 334 707 254" fill="none" stroke="var(--white)" stroke-width="6"/>
    <line x1="235" y1="0" x2="235" y2="546" stroke="var(--fold)" stroke-width="1" stroke-dasharray="8 6"/>
    <line x1="471" y1="0" x2="471" y2="546" stroke="var(--fold)" stroke-width="1" stroke-dasharray="8 6"/>
  </svg>

  <div class="pill pill--students">Students</div>
  <ul class="student-list">
    <li>Students are adults in need of</li>
    <li class="bullet">Basic literacy skills</li>
    <li class="bullet">Pre-HSE skills</li>
    <li class="bullet">Conversational English</li>
    <li class="bullet">Tutoring is free of charge</li>
    <li class="bullet">Tutoring is one-on-one</li>
    <li class="bullet">Flexible scheduling during<br>&nbsp;&nbsp;library hours</li>
    <li class="bullet">Lessons focus on student goals</li>
    <li>&nbsp;&nbsp;If you can read, you can tutor!</li>
  </ul>

  <div class="brand-tab"><div class="brand-name"><span class="brand-mark"></span>Reading Bridge<br>Partners</div></div>
  <div class="cta-box">Don't waste a moment!<br>Contact us today to<br>learn more.</div>
  <div class="contact">
    Volunteer desk: 555-014-2210<br>Riverton, Oakdale &amp; Lake<br>Point: 555-014-3387
    <div class="email">literacy@rivertonlibrary.org</div>
  </div>

  <div class="brand-badge"><div class="brand-name"><span class="brand-mark"></span>Reading Bridge<br>Partners</div></div>
  <div class="pill pill--volunteer">Volunteer</div>
  <div class="volunteer-copy">Enrich a life!<br>Help an adult learn<br><span class="spread">to read, write or</span><br>speak English</div>
</section>

<section class="sheet sheet--outside">
  <svg class="sheet-art" viewBox="0 0 707 546">
    <defs>
      <linearGradient id="groupPhoto" x1="0" y1="0" x2="1" y2="0">
        <stop offset="0" stop-color="#7fb59a"/><stop offset="0.3" stop-color="#8a3b3e"/><stop offset="0.55" stop-color="#d8d4cc"/><stop offset="0.8" stop-color="#e38aa0"/><stop offset="1" stop-color="#9cb8d8"/>
      </linearGradient>
    </defs>
    <path role="img" aria-label="Photo: five smiling adults of diverse backgrounds around a library table with books" d="M0 0 H707 V150 Q560 300 0 322 Z" fill="url(#groupPhoto)"/>
    <path d="M0 328 Q560 306 707 154" fill="none" stroke="var(--white)" stroke-width="8"/>
    <line x1="235" y1="0" x2="235" y2="546" stroke="var(--fold)" stroke-width="1" stroke-dasharray="8 6"/>
    <line x1="471" y1="0" x2="471" y2="546" stroke="var(--fold)" stroke-width="1" stroke-dasharray="8 6"/>
  </svg>

  <div class="pill pill--tutors">Tutors</div>
  <ul class="tutor-points">
    <li>No special skills or degrees needed — just a degree of caring!</li>
    <li>Training offered throughout the year</li>
    <li>Tutors meet students weekly at a library</li>
    <li>Instructional materials provided</li>
    <li>Ongoing support available</li>
    <li class="closing">Teach an adult to read and you'll change a life forever.</li>
  </ul>
</section>

</body>
</html>
```